BrightNomadRx.com Blog Design (Travel, Lifestyle, and Life Hacking blog)

I am launching a lifestyle blog about my life. I'm a doctor who travels the world trying the best restaurants, airlines and trying to have as much fun as possible. I also invest in startups, and am always trying new tricks to make life better. I also plan to write about various other topics, but essentially it is about travel, lifestyle and medicine. I need a creative and really awesome looking design for a new wordpress blog called BrightNomadRx

Target Market(s)

Physicians, Entrepreneurs, Travellers

Industry/Entity Type

Airlines

Number of Pages Required

1 page

Font styles to use
Serif

Requirements
Must have
• Slick looking graphics with a highly professional modern feel

```html
<!DOCTYPE html>
<html lang="en">
<head>
<meta charset="utf-8">
<title>BrightNomadRx – Travel, Lifestyle &amp; Medicine</title>
<link rel="stylesheet" href="https://fonts.googleapis.com/css2?family=Oswald:wght@400;500;600&family=Open+Sans:wght@400;600;700&display=swap">
<style>
:root{
  --teal:#46b5a7;
  --teal-dark:#3a9e92;
  --ink:#222;
  --muted:#888;
  --rule:#dcdcdc;
  --panel:#f1f1f1;
  --footer:#333;
  --white:#fff;
}
*{box-sizing:border-box;margin:0;padding:0}
html,body{width:1200px;height:2818px;overflow:hidden}
body{position:relative;background:var(--white);font-family:"Open Sans",Arial,sans-serif;color:var(--ink)}
.head{font-family:"Oswald",Arial,sans-serif;text-transform:uppercase}

/* header */
.masthead{position:absolute;top:0;left:0;width:1200px;height:99px;display:flex;align-items:center;justify-content:center}
.brand{font-family:"Oswald",Arial,sans-serif;font-weight:500;font-size:40px;color:#111;letter-spacing:1px}
.mainnav{position:absolute;top:99px;left:0;width:1200px;height:37px;background:var(--teal);display:flex;align-items:center;padding-left:292px;gap:42px}
.mainnav a{color:var(--white);text-decoration:none;font-family:"Oswald",Arial,sans-serif;font-size:13px;text-transform:uppercase;letter-spacing:.5px}
.mainnav svg{display:block}

/* hero */
.hero{position:absolute;top:136px;left:0;width:1200px;height:392px;background:linear-gradient(180deg,#9cb6cc 0%,#c7d6e2 45%,#8ea7b8 70%,#5d7788 100%)}
.hero-card{position:absolute;top:115px;left:312px;width:576px;height:144px;background:rgba(255,255,255,.93);text-align:center;padding-top:16px}
.hero-card .kicker{font-size:15px;font-style:italic;text-decoration:underline;color:#333}
.hero-card h1{font-family:"Open Sans",Arial,sans-serif;font-weight:700;font-size:19px;line-height:25px;margin-top:10px}
.hero-card .meta{display:flex;justify-content:space-between;padding:0 50px;margin-top:12px;font-size:12px;color:#444}

/* category tiles */
.tiles{position:absolute;top:554px;left:160px;width:880px;height:198px;display:flex;justify-content:space-between}
.tile{width:278px;height:198px;border:4px solid #d7d7d7;display:flex;align-items:center;justify-content:center;color:var(--white);font-family:"Oswald",Arial,sans-serif;font-size:20px;font-weight:500;letter-spacing:1px}
.tile-lifestyle{background:linear-gradient(160deg,#6f8ba6,#3e5a72)}
.tile-travels{background:linear-gradient(160deg,#8a96a0,#4f5f6c)}
.tile-fun{background:linear-gradient(160deg,#d9b48a,#8e6e56)}

/* section titles */
.sec-title{font-family:"Oswald",Arial,sans-serif;font-size:17px;text-transform:uppercase;color:#111;border-bottom:2px solid var(--rule);padding-bottom:6px}

/* latest */
.latest{position:absolute;top:772px;left:160px;width:430px}
.latest-list{margin-top:12px;display:flex;flex-direction:column;gap:22px}
.feature{position:relative;height:331px}
.feature .band{position:absolute;left:0;bottom:0;width:100%;background:rgba(0,0,0,.55);color:var(--white);padding:14px 14px 12px}
.feature h2{font-family:"Oswald",Arial,sans-serif;font-weight:500;font-size:19px;text-transform:uppercase}
.feature p{font-size:11px;line-height:15px;margin-top:4px}
.feature-hills{background:linear-gradient(180deg,#7ab8de 0%,#cfe3c8 45%,#6f9c3e 75%,#3f6424 100%)}
.feature-family{background:linear-gradient(160deg,#e7ddd0 0%,#c9a98c 50%,#6f8da8 100%)}
.row{display:flex;height:122px;gap:14px}
.thumb{position:relative;width:204px;height:122px;flex:none}
.tag{position:absolute;left:0;top:14px;background:var(--teal);color:var(--white);font-size:10px;padding:3px 12px 3px 6px;width:72px}
.row .text h3{font-family:"Oswald",Arial,sans-serif;font-weight:400;font-size:12.5px;line-height:15px;text-transform:uppercase}
.row .text .date{font-size:9px;color:var(--muted);margin:3px 0 6px}
.row .text p{font-size:10.5px;line-height:14px;color:#777}
.dot{display:inline-block;width:9px;height:9px;border-radius:50%;border:1px solid #888;vertical-align:middle}

/* most viewed */
.mostviewed{position:absolute;top:772px;left:608px;width:132px}
.mv-list{margin-top:12px;display:flex;flex-direction:column;gap:20px}
.mv-item .thumb{width:132px;height:98px}
.mv-item .tag{top:auto;bottom:6px;left:auto;right:0;width:74px;padding-left:10px}
.mv-item h3{font-family:"Oswald",Arial,sans-serif;font-weight:400;font-size:12px;line-height:14px;text-transform:uppercase;margin-top:8px}
.mv-item p{font-size:10.5px;line-height:14px;color:#777;margin-top:4px}

/* sidebar */
.sidebar{position:absolute;top:778px;left:761px;width:279px}
.panel{background:var(--panel);border-top:42px solid var(--teal);position:relative}
.panel-title{position:absolute;top:-42px;left:0;height:42px;line-height:42px;padding-left:14px;color:var(--white);font-family:"Oswald",Arial,sans-serif;font-size:17px;text-transform:uppercase;border-bottom:3px solid #fff}
.pop{padding:16px 14px 10px}
.pop li{display:flex;gap:12px;list-style:none;margin-bottom:17px}
.pop .pic{width:38px;height:38px;flex:none}
.pop p{font-size:10.5px;line-height:14px;color:#555}
.topics{padding:14px 14px 4px;margin-top:20px}
.topics li{list-style:none;display:flex;gap:12px;margin-bottom:16px}
.topics .pic{width:72px;height:74px;flex:none}
.topics h4{font-family:"Oswald",Arial,sans-serif;font-weight:400;font-size:15px}
.topics p{font-size:9.5px;line-height:13px;color:#666;margin-top:4px}
.video{margin-top:16px;padding:14px 14px 14px}
.video .screen{height:150px;background:linear-gradient(160deg,#d4d8dc,#8c99a3);position:relative}
.video .play{position:absolute;left:50%;top:50%;width:36px;height:26px;margin:-13px 0 0 -18px;background:#222;border-radius:6px}
.video .play::after{content:"";position:absolute;left:14px;top:7px;border-left:11px solid #fff;border-top:6px solid transparent;border-bottom:6px solid transparent}
.video h4{font-family:"Oswald",Arial,sans-serif;font-weight:400;font-size:14px;margin-top:12px}
.video .date{font-size:9px;color:var(--muted)}
.ad-box{margin-top:18px;height:232px;background:linear-gradient(180deg,#2f6fd8,#1e4fb0);padding:18px 16px;color:var(--white);position:relative}
.ad-box .pitch{font-size:26px;line-height:29px;font-weight:400}
.ad-box .pitch b{color:#8ef0ff;font-weight:600}
.ad-box .adname{position:absolute;left:16px;bottom:30px;font-size:17px;font-weight:700;color:#fff}
.ad-box .adurl{position:absolute;left:16px;bottom:10px;font-size:9px;color:#cfe0ff}
.ad-box .handset{position:absolute;right:18px;bottom:30px;width:70px;height:70px;border-radius:50%;background:#eaf2ff}
.news{margin-top:20px;padding:14px 14px 16px}
.news .intro{font-size:10px;line-height:14px;color:#666}
.news ul{margin-top:10px}
.news li{list-style:none;display:flex;align-items:center;gap:10px;font-family:"Oswald",Arial,sans-serif;font-weight:500;font-size:15px;margin-bottom:6px}
.news li span{width:12px;height:12px;border:1px solid #999;background:#fff}
.field{height:36px;background:#fff;border:1px solid #ddd;font-size:10px;color:#888;padding:11px 10px;margin-top:12px}
.btn{margin-top:14px;height:38px;background:#444;border-radius:4px;color:#fff;text-align:center;line-height:38px;font-family:"Oswald",Arial,sans-serif;font-size:13px}

/* bottom ad */
.banner{position:absolute;top:2419px;left:160px;width:430px;height:66px;display:flex;align-items:center;gap:20px;background:#fff}
.banner .name{font-family:"Oswald",Arial,sans-serif;font-weight:600;font-size:34px;color:#1c1c1c;letter-spacing:1px}
.banner .line{font-size:15px;line-height:18px;color:#555;font-style:italic}
.banner .pic{width:60px;height:60px;background:linear-gradient(160deg,#9ec7e5,#6b88a0);margin-left:auto}

/* footer */
.site-footer{position:absolute;top:2555px;left:0;width:1200px;height:263px;background:var(--footer);color:#ddd}
.site-footer .brand{color:#fff;font-size:32px;position:absolute;left:160px;top:32px}
.copy{position:absolute;left:160px;top:96px;font-size:11px;line-height:18px}
.fcol{position:absolute;top:34px}
.fcol h5{font-family:"Oswald",Arial,sans-serif;font-weight:500;font-size:15px;color:var(--teal);margin-bottom:12px}
.fcol li{list-style:none;font-size:11px;line-height:24px}
.social{display:flex;gap:7px;margin-bottom:10px}
.social span{width:18px;height:18px;border-radius:50%}
</style>
</head>
<body>

<header class="masthead"><div class="brand">BrightNomadRx</div></header>

<nav class="mainnav">
  <a href="#" aria-label="Home"><svg width="14" height="13" viewBox="0 0 14 13"><path d="M7 0 0 6h2v7h4V9h2v4h4V6h2z" fill="#fff"/></svg></a>
  <a href="#">Lifestyle</a><a href="#">Best Travels</a><a href="#">Health</a><a href="#">Medicine</a><a href="#">Airlines</a><a href="#">Restaurants</a>
</nav>

<section class="hero" role="img" aria-label="Traveller with backpack taking a selfie above the sea under a cloudy sky">
  <div class="hero-card">
    <div class="kicker">Life Style</div>
    <h1>Travels The World Trying The Best Restaurants,<br>Airlines,Lifestyle And Medicine Etc.</h1>
    <div class="meta"><span>Dec 24, 2016</span><span>By : Marla K. Denholm</span><span>12 Comments</span></div>
  </div>
</section>

<section class="tiles">
  <div class="tile tile-lifestyle" role="img" aria-label="Friends on a beach">LIFESTYLE</div>
  <div class="tile tile-travels" role="img" aria-label="People walking on a beach">TRAVELS</div>
  <div class="tile tile-fun" role="img" aria-label="Group with balloons">FUN</div>
</section>

<main class="latest">
  <h2 class="sec-title">Latest Articles</h2>
  <div class="latest-list">
    <article class="feature feature-hills" role="img" aria-label="Man with raised arms on a green hilltop">
      <div class="band"><h2>Donec vel arcu pellentesque, consequat nulla</h2><p>But I must explain to you how all this mistaken idea of denouncing pleasure and praising pain was born and I will give you a complete account of the</p></div>
    </article>
    <article class="row"><div class="thumb" role="img" aria-label="Airliner tail fin" style="background:linear-gradient(160deg,#cfd8de,#b33b2e)"><span class="tag">Airlines</span></div>
      <div class="text"><h3>Sed ut perspiciatis unde omnis iste natus error sit voluptatem</h3><div class="date">June 25th 2015 | 0 Comments</div><p>At vero eos et accusamus et iusto odio dignissimos ducimus qui blanditiis praesentium voluptatum deleniti atque corrupti quos dolores et <span class="dot"></span></p></div></article>
    <article class="row"><div class="thumb" role="img" aria-label="Beach chairs at sunset" style="background:linear-gradient(180deg,#f0a24a,#5a86b8)"><span class="tag">Travel</span></div>
      <div class="text"><h3>Duis aute irure dolor in reprehenderit in voluptate velit esse cillum dolore</h3><div class="date">June 26th 2015 | 0 Comments</div><p>At vero eos et accusamus et iusto odio dignissimos ducimus qui blanditiis praesentium voluptatum deleniti atque corrupti quos dolores et <span class="dot"></span></p></div></article>
    <article class="feature feature-family" role="img" aria-label="Family travelling on an airplane">
      <div class="band"><h2>Temporibus autem quibusdam et aut officiis</h2><p>But I must explain to you how all this mistaken idea of denouncing pleasure and praising pain was born and I will give you a complete account of the</p></div>
    </article>
    <article class="row"><div class="thumb" role="img" aria-label="Kayaking on a lake" style="background:linear-gradient(180deg,#8fc6e6,#2f7fb0)"><span class="tag">Lifestyle</span></div>
      <div class="text"><h3>But who has any right to find fault</h3><div class="date">June 25th 2015 | 0 Comments</div><p>At vero eos et accusamus et iusto odio dignissimos ducimus qui blanditiis praesentium voluptatum deleniti atque corrupti quos <span class="dot"></span></p></div></article>
    <article class="row"><div class="thumb" role="img" aria-label="Hand holding a stethoscope" style="background:linear-gradient(160deg,#f3f3f3,#bfc6cc)"><span class="tag">Health</span></div>
      <div class="text"><h3>Quis autem vel eum iure reprehenderit</h3><div class="date">June 26th 2015 | 0 Comments</div><p>At vero eos et accusamus et iusto odio dignissimos ducimus qui blanditiis praesentium voluptatum deleniti atque corrupti quos <span class="dot"></span></p></div></article>
    <article class="row"><div class="thumb" role="img" aria-label="Restaurant dining room" style="background:linear-gradient(160deg,#c98a4a,#6b3c1e)"><span class="tag">Restaurants</span></div>
      <div class="text"><h3>Ut aut reiciendis voluptatibus maiores alias consequatur aut</h3><div class="date">June 03rd 2015 | 0 Comments</div><p>At vero eos et accusamus et iusto odio dignissimos ducimus qui blanditiis praesentium voluptatum deleniti atque corrupti quos <span class="dot"></span></p></div></article>
    <article class="row"><div class="thumb" role="img" aria-label="Couple on a sunny beach" style="background:linear-gradient(180deg,#6fb8e6,#e9d6a8)"><span class="tag">Travel</span></div>
      <div class="text"><h3>The wise man therefore always holds in these matters to this principle of</h3><div class="date">June 26th 2015 | 0 Comments</div><p>At vero eos et accusamus et iusto odio dignissimos ducimus qui blanditiis praesentium voluptatum deleniti atque corrupti quos <span class="dot"></span></p></div></article>
  </div>
</main>

<aside class="mostviewed">
  <h2 class="sec-title">Most Viewed</h2>
  <div class="mv-list">
    <article class="mv-item"><div class="thumb" role="img" aria-label="Woman in a cabin" style="background:linear-gradient(160deg,#cbb6a6,#6f5448)"><span class="tag">Airlines</span></div><h3>Excepteur sint occaecat cupidatat non proident</h3><p>At vero eos et accusamus et iusto odio dignissimos ducimus qui <span class="dot"></span></p></article>
    <article class="mv-item"><div class="thumb" role="img" aria-label="Traveller at the sea" style="background:linear-gradient(180deg,#8ab8d8,#3d6f90)"><span class="tag">Travels</span></div><h3>Neque porro quisquam est, qui dolorem ipsum</h3><p>At vero eos et accusamus et iusto odio dignissimos ducimus qui blanditiis</p></article>
    <article class="mv-item"><div class="thumb" role="img" aria-label="Person jumping on a beach" style="background:linear-gradient(180deg,#9fd0ee,#e6d3a4)"><span class="tag">Lifestyle</span></div><h3>To take a trivial example, which of us</h3><p>At vero eos et accusamus et iusto odio dignissimos ducimus qui blanditiis <span class="dot"></span></p></article>
    <article class="mv-item"><div class="thumb" role="img" aria-label="Chef cooking" style="background:linear-gradient(160deg,#d9a15e,#5b3a20)"><span class="tag">Restaurants</span></div><h3>Itaque earum rerum hic tenetur a sapiente</h3><p>At vero eos et accusamus et iusto odio dignissimos ducimus qui blanditiis <span class="dot"></span></p></article>
    <article class="mv-item"><div class="thumb" role="img" aria-label="Windsurfer on blue water" style="background:linear-gradient(180deg,#7fc0ea,#2a78b4)"><span class="tag">Lifestyle</span></div><h3>To take a trivial example, which of us ever undertakes laborious physical</h3><p>At vero eos et accusamus et iusto odio dignissimos ducimus qui</p></article>
    <article class="mv-item"><div class="thumb" role="img" aria-label="Plated food on a table" style="background:linear-gradient(160deg,#b98256,#4d2e1a)"><span class="tag">Restaurants</span></div><h3>To take a trivial example, which of us</h3><p>At vero eos et accusamus et iusto odio dignissimos ducimus qui blanditiis <span class="dot"></span></p></article>
    <article class="mv-item"><div class="thumb" role="img" aria-label="Doctor in a clinic" style="background:linear-gradient(160deg,#e9ecef,#9aa8b2)"><span class="tag">Health</span></div><h3>Excepteur sint occaecat cupidatat non proident</h3><p>At vero eos et accusamus et iusto odio dignissimos ducimus qui <span class="dot"></span></p></article>
  </div>
</aside>

<aside class="sidebar">
  <section class="panel"><h2 class="panel-title">Popular Articles</h2>
    <ul class="pop">
      <li><div class="pic" role="img" aria-label="Article photo" style="background:#b49a86"></div><p>Lorem ipsum dolor sit amet, consectetur adipiscing elit.</p></li>
      <li><div class="pic" role="img" aria-label="Article photo" style="background:#8aa6ba"></div><p>Sed aliquet justo ut maximus vestibulum.</p></li>
      <li><div class="pic" role="img" aria-label="Article photo" style="background:#c7a48a"></div><p>Sed et risus non leo aliquam faucibus nec sed nisl.</p></li>
      <li><div class="pic" role="img" aria-label="Article photo" style="background:#9a8a7e"></div><p>Vivamus pretium augue sit suscipit mollis.</p></li>
      <li><div class="pic" role="img" aria-label="Article photo" style="background:#a7b9c6"></div><p>Sed aliquet justo ut maximus vestibulum.</p></li>
    </ul>
  </section>
  <section class="panel topics" style="padding:0"><h2 class="panel-title">Topics / Categories</h2>
    <ul style="padding:14px 14px 4px">
      <li><div class="pic" role="img" aria-label="Healthy food bowl" style="background:linear-gradient(160deg,#e8d9a8,#8fae5c)"></div><div><h4>DIET</h4><p>Sed ut perspiciatis unde omnis iste natus error sit voluptatem accusantium doloremque laudantium.</p></div></li>
      <li><div class="pic" role="img" aria-label="Medical equipment" style="background:linear-gradient(160deg,#f2f2f2,#c44c4c)"></div><div><h4>MEDICINE</h4><p>Sed ut perspiciatis unde omnis iste natus error sit voluptatem accusantium doloremque laudantium.</p></div></li>
      <li><div class="pic" role="img" aria-label="Couple at sunset" style="background:linear-gradient(180deg,#7d8fb4,#2c2f44)"></div><div><h4>LIFESTYLE</h4><p>Sed ut perspiciatis unde omnis iste natus error sit voluptatem accusantium doloremque laudantium.</p></div></li>
      <li><div class="pic" role="img" aria-label="Airline cabin crew" style="background:linear-gradient(160deg,#c8c2bc,#6e5e56)"></div><div><h4>AIRLINES</h4><p>Sed ut perspiciatis unde omnis iste natus error sit voluptatem accusantium doloremque laudantium.</p></div></li>
    </ul>
  </section>
  <section class="panel video"><h2 class="panel-title">Popular Video</h2>
    <div class="screen" role="img" aria-label="Video still of a family at home"><span class="play"></span></div>
    <h4>AIRLINES</h4><div class="date">25TH DEC 2016</div>
  </section>
  <div class="ad-box">
    <p class="pitch">Enterprise quality <b>voicemail</b> at an affordable price.</p>
    <span class="handset" role="img" aria-label="Telephone handset"></span>
    <span class="adname">VoxLedger</span><span class="adurl">www.voxledger.com</span>
  </div>
  <section class="panel news"><h2 class="panel-title">Subscribe To Our Newsletter</h2>
    <p class="intro">Enter your email address below to receive site offers, discounts, and promotions from us.</p>
    <ul><li><span></span>Lorem ipsum dolor</li><li><span></span>Lorem ipsum dolor</li><li><span></span>Lorem ipsum dolor</li><li><span></span>Lorem ipsum dolor</li><li><span></span>Lorem ipsum dolor</li></ul>
    <div class="field">Name</div><div class="field">Email</div>
    <div class="btn">SUBSCRIBE</div>
  </section>
</aside>

<div class="banner">
  <span class="name">GRIDFORGE</span>
  <span class="line">Let's build<br>something AWESOME</span>
  <span class="pic" role="img" aria-label="Small promotional illustration"></span>
</div>

<footer class="site-footer">
  <div class="brand">BrightNomadRx</div>
  <p class="copy">Copyright © 2016 BrightNomadRx<br>All Rights Reserved.</p>
  <div class="fcol" style="left:495px"><h5>GENERAL</h5><ul><li>Lifestyle</li><li>Best travels</li><li>Health</li><li>Medicine</li><li>Airlines</li><li>Restaurants</li></ul></div>
  <div class="fcol" style="left:688px"><h5>OTHER</h5><ul><li>Avoid Fraud</li><li>Contact Us</li><li>Reprints &amp; Permissions</li><li>Customer Service</li><li>Manage Email Preferences</li><li>Copyright Notice</li></ul></div>
  <div class="fcol" style="left:932px"><h5>FOLLOW US</h5>
    <div class="social"><span style="background:#3aa7e0"></span><span style="background:#3b5b98"></span><span style="background:#d9473b"></span><span style="background:#cc2a2a"></span></div>
    <ul><li>Term and Condition</li><li>Privacy Policy</li></ul></div>
</footer>

</body>
</html>
```